Cover for Where the Quiet River Bends Beyond Our Morning

Cover for a book that describes everything that happens to a person, from pre-birth life plans through growing in compassion and wisdom to death and living in the afterlife. The information is revealed in messages from people living in the life after this life. The title is Lanterns Along the Hidden Stair of Every Soul: Gathered from Voices Dwelling in the Further Meadow. Author is T. Morven Ashdale. Book size is 6 by 9.

Target Market(s)

General

Font styles to use
Serif

```html
<!DOCTYPE html>
<html lang="en">
<head>
<meta charset="utf-8">
<title>Lanterns Along the Hidden Stair of Every Soul — T. Morven Ashdale</title>
<link rel="stylesheet" href="https://fonts.googleapis.com/css2?family=Crimson+Pro:wght@400;500&display=swap">
<style>
  :root {
    --night: #1a1024;
    --dusk: #3a1f3c;
    --ember: #c9502e;
    --glow: #f2a276;
    --light: #fbeee2;
    --coral: #ee6a4d;
    --white: #ffffff;
    --earth: #2b2638;
  }
  * { margin: 0; padding: 0; box-sizing: border-box; }
  html, body { width: 800px; height: 1200px; overflow: hidden; background: var(--night); }
  .cover {
    position: relative;
    width: 800px;
    height: 1200px;
    overflow: hidden;
    font-family: "Crimson Pro", "Times New Roman", serif;
    color: var(--white);
    text-align: center;
  }
  .cover-art {
    position: absolute;
    inset: 0;
    background:
      radial-gradient(ellipse 120px 420px at 50% 42%, rgba(251,238,226,0.85), rgba(242,162,118,0.5) 45%, transparent 100%),
      radial-gradient(ellipse 340px 520px at 50% 60%, rgba(242,162,118,0.75), rgba(201,80,46,0.55) 50%, transparent 100%),
      radial-gradient(ellipse 520px 600px at 50% 55%, rgba(201,80,46,0.55), rgba(58,31,60,0.6) 60%, transparent 100%),
      linear-gradient(180deg, var(--night) 0%, var(--dusk) 45%, var(--dusk) 70%, var(--night) 100%);
  }
  .cover-art .planet {
    position: absolute;
    left: -60px;
    top: 940px;
    width: 920px;
    height: 600px;
    border-radius: 50%;
    background: radial-gradient(ellipse at 50% 20%, #4a3a52, var(--earth) 55%, #15111d);
    box-shadow: 0 -6px 30px rgba(242,162,118,0.6);
  }
  .title-block { position: absolute; top: 122px; left: 0; right: 0; }
  .title-lead {
    display: flex;
    align-items: center;
    justify-content: center;
    gap: 38px;
    color: var(--coral);
    font-size: 46px;
    font-weight: 500;
    letter-spacing: 1px;
    line-height: 1;
  }
  .title-lead .rule { width: 100px; height: 1.5px; background: var(--white); }
  .title-main {
    margin-top: 22px;
    font-size: 44px;
    font-weight: 400;
    line-height: 60px;
    letter-spacing: 1px;
  }
  .subtitle {
    margin-top: 20px;
    font-size: 26px;
    font-weight: 500;
    letter-spacing: 0.8px;
  }
  .author {
    position: absolute;
    left: 0; right: 0;
    top: 1078px;
    color: var(--coral);
    font-size: 40px;
    font-weight: 500;
    letter-spacing: 6px;
  }
</style>
</head>
<body>
  <main class="cover">
    <div class="cover-art" role="img" aria-label="Glowing figure rising in a beam of light above cracked stone figures huddled on the Earth, against a starry ember sky">
      <div class="planet"></div>
    </div>
    <header class="title-block">
      <h1>
        <span class="title-lead"><span class="rule"></span>LANTERNS ALONG<span class="rule"></span></span>
        <span class="title-main" style="display:block">THE HIDDEN STAIR<br>OF EVERY SOUL</span>
      </h1>
      <p class="subtitle">Gathered from Voices Dwelling in the Further Meadow</p>
    </header>
    <p class="author">T. MORVEN ASHDALE</p>
  </main>
</body>
</html>
```